BrovaLT BIZ Card, email signature & Stationary

Professional business cards, email signatures and ms word letterhead

Target Market(s)

business owners

Industry/Entity Type

cloud hosting

Contact Information for Business Card

name title office phone number , direct line, fax email address web site

Font styles to use
Other font styles liked:
• something that compliments font in logo

```html
<!DOCTYPE html>
<html lang="en">
<head>
<meta charset="utf-8">
<title>BrovaLT Business Card</title>
<link rel="stylesheet" href="https://fonts.googleapis.com/css2?family=Montserrat:wght@300;400;800&display=swap">
<style>
  :root {
    --page: #ffffff;
    --card-white: #ffffff;
    --card-grey: #b3b3b3;
    --ink: #000000;
    --text-light: #ffffff;
  }
  * { margin: 0; padding: 0; box-sizing: border-box; }
  html, body {
    width: 1200px;
    height: 1200px;
    overflow: hidden;
    background: var(--page);
    font-family: "Montserrat", Arial, sans-serif;
  }
  .card {
    position: absolute;
    left: 304px;
    width: 600px;
    height: 343px;
    overflow: hidden;
    box-shadow: 0 2px 8px rgba(0, 0, 0, 0.35);
  }
  .card-front { top: 211px; background: var(--card-white); }
  .card-back { top: 653px; background: var(--card-grey); }
  .card-pattern {
    position: absolute;
    inset: 0;
    width: 100%;
    height: 100%;
  }
  .brand-name {
    position: absolute;
    transform: translate(-50%, -50%);
    font-weight: 800;
    text-transform: uppercase;
    letter-spacing: 0.04em;
    white-space: nowrap;
    line-height: 1;
  }
  .card-front .brand-name { left: 299px; top: 171px; font-size: 44px; color: var(--ink); }
  .card-back .brand-name { left: 426px; top: 238px; font-size: 34px; color: var(--text-light); }
  .holder-name {
    position: absolute;
    left: 57px;
    top: 88px;
    font-size: 35px;
    font-weight: 800;
    color: var(--text-light);
    line-height: 1;
    letter-spacing: 0.01em;
  }
  .holder-title {
    position: absolute;
    left: 58px;
    top: 124px;
    font-size: 19px;
    font-weight: 300;
    color: var(--text-light);
    line-height: 1;
  }
  .contact-rule {
    position: absolute;
    left: 45px;
    top: 181px;
    width: 9px;
    height: 138px;
    background: var(--ink);
  }
  .contact-list {
    position: absolute;
    left: 64px;
    top: 182px;
    list-style: none;
    font-size: 14px;
    font-weight: 400;
    color: var(--text-light);
    line-height: 14.5px;
  }
  .contact-list li { margin-bottom: 14.5px; }
  .contact-list li:last-child { margin-bottom: 0; }
</style>
</head>
<body>
  <section class="card card-front">
    <svg class="card-pattern" viewBox="0 0 960 549" preserveAspectRatio="none" aria-hidden="true">
      <g fill="#b3b3b3">
        <polygon points="659,0 857,175 960,85 960,0 857,90 756,0"/>
        <polygon points="801,0 857,49 912,0"/>
        <polygon points="0,411 106,318 367,549 271,549 106,403 0,496"/>
        <polygon points="0,536 106,443 225,549 129,549 106,528 83,549 0,549"/>
      </g>
    </svg>
    <div class="brand-name">BrovaLT</div>
  </section>

  <section class="card card-back">
    <svg class="card-pattern" viewBox="0 0 960 549" preserveAspectRatio="none" aria-hidden="true">
      <g fill="#ffffff">
        <polygon points="588,0 857,238 960,148 960,29 857,118 722,0"/>
        <polygon points="786,0 857,62 927,0"/>
      </g>
    </svg>
    <h1 class="holder-name">ALEXIS DOE</h1>
    <p class="holder-title">Graphic Designer</p>
    <div class="contact-rule"></div>
    <ul class="contact-list">
      <li>+011123 456 789</li>
      <li>+011123 456 789</li>
      <li>address goes here<br>your street, Road123</li>
      <li>name@email.com<br>yourwebsite.com</li>
    </ul>
    <div class="brand-name">BrovaLT</div>
  </section>
</body>
</html>
```